依頼詳細
茶の(平袋アルミ袋)入りの商品を依頼させていただきます。どこかに、金色が使われ、高級感があり、純和風な感じを出していただきたく思います。外国人(アメリカ、中国)の方が、日本を創造でき、日本人にも、心地よい商品を希望します。下地の銀色を除き、3色程度でお願いします。
記載項目
110mm×22.5mm(表面)(写真参照、後ろに絵はつながっています。)
希望イメージ
シンプル 複雑
単色 カラフル
暗い 明るい
日常 高級
遊び心 厳粛
未来的 伝統的
女性的 男性的
希望する色
仏事に使われる事が多いので、なるべく赤は避け、健康的で、高級感が欲しいです。
納品ファイル
• 高解像度JPG (.jpg)
• イラストレーター形式 (.ai)
• フォトショップ形式 (.psd)
補足説明
相手をもてなす気持を大切に思っております。一期一会にもあるように、急須の先にいる方に、最後の一滴まで美味しく飲んでいただけるような気持が届く、パッケージになれば、幸いです。一滴、ひとしずく、露をイメージした、デザインがいいです。(どこかでつかわれている習字の一筆書きの丸のようなイメージとかも良いなと感じています。(真似はだめですが・・・。))また、真逆もありだと思います。
依頼公開後の追記内容
配色の金色については、ちりばめるか、装飾程度で、いやらしさのない方がよいです。
商品名は、シールや、後印刷で行いますので、あまり誇張のない方がいいです。
初めてのご依頼ですので、知らないことが多く、無礼なことをしていてすみませんでした。変更依頼は、決定した後とは思いませんでした。皆さんに素晴らしいアイデアを頂いて、本当に幸せに感じております。出張で、3日不在です。帰社してから、選定させていただきたく思います。ありがとうございます!
■ 選んだ理由

「シンプルで、金色が使われ、高級感があり、純和風な感じを出し、日本を想像させるパッケージ」依頼だったのですが、そのものズバリといった感じでした。お茶の袋は、市販品が沢山あり、ありふれたものが多く、存在感のあるご提案を採用させて頂きました。

■ 提案者全員のお礼・コメント

初めての依頼だったのですが、快く引き受けてくださった皆様に、先ず、本当にありがとうございました。感謝を申し上げます。皆さまの素晴らしいデザインを拝見させていただき、技術の高さと想像力の豊富さを感じさせていただきました。ありがとうございました。

```html
<!DOCTYPE html>
<html lang="ja">
<head>
<meta charset="utf-8">
<title>しずくの里のおくりもの</title>
<link rel="stylesheet" href="https://fonts.googleapis.com/css2?family=Shippori+Mincho:wght@500&display=swap">
<style>
  :root {
    --ink: #0b0b0b;
    --pattern-tone: #262626;
    --pattern-line: #3a3a3a;
    --olive: #6b6420;
    --cream: #ece8c6;
    --drop: #b7c23a;
    --gold: #e0922a;
    --gold-light: #f0b042;
    --petal: #f4f1e4;
    --label-bg: #ffffff;
    --label-ink: #5f7d2a;
  }
  * { margin: 0; padding: 0; box-sizing: border-box; }
  html, body { width: 1200px; height: 2516px; overflow: hidden; background: var(--ink); }
  .package {
    position: relative;
    width: 1200px;
    height: 2516px;
    background: var(--ink);
    overflow: hidden;
  }
  .flower-pattern {
    position: absolute;
    inset: 0;
    background:
      radial-gradient(circle at 12% 12%, var(--pattern-tone), transparent 14%),
      radial-gradient(circle at 88% 10%, var(--pattern-tone), transparent 14%),
      radial-gradient(circle at 90% 38%, var(--pattern-tone), transparent 14%),
      radial-gradient(circle at 8% 48%, var(--pattern-tone), transparent 13%),
      radial-gradient(circle at 85% 66%, var(--pattern-tone), transparent 14%),
      radial-gradient(circle at 14% 80%, var(--pattern-tone), transparent 14%),
      radial-gradient(circle at 80% 92%, var(--pattern-tone), transparent 13%),
      var(--ink);
  }
  .gold-scatter {
    position: absolute;
    inset: 0;
    width: 1200px;
    height: 2516px;
  }
  .gold-scatter rect { fill: var(--gold); }
  .gold-scatter rect.light { fill: var(--gold-light); }
  .tea-band {
    position: absolute;
    left: 372px;
    top: 0;
    width: 448px;
    height: 2340px;
    background: var(--olive);
  }
  .camellia {
    position: absolute;
    background: radial-gradient(circle, var(--petal) 35%, #d8d4c0 75%);
    border-radius: 50%;
  }
  .camellia--top { left: 560px; top: 0; width: 250px; height: 290px; border-radius: 0 0 50% 50%; }
  .camellia--bottom { left: 400px; top: 1980px; width: 420px; height: 330px; }
  .dewdrop { position: absolute; left: 396px; top: 430px; width: 40px; height: 60px; }
  .product-name {
    position: absolute;
    left: 584px;
    top: 300px;
    transform: translateX(-50%);
    writing-mode: vertical-rl;
    font-family: "Shippori Mincho", serif;
    font-weight: 500;
    font-size: 120px;
    letter-spacing: 28px;
    line-height: 1;
    color: var(--cream);
  }
  .maker-label {
    position: absolute;
    left: 592px;
    top: 2370px;
    width: 228px;
    height: 130px;
    background: var(--label-bg);
    display: flex;
    align-items: center;
    justify-content: center;
    gap: 10px;
    font-family: "Shippori Mincho", serif;
    font-weight: 500;
    font-size: 40px;
    color: var(--label-ink);
  }
  .maker-label .mark { width: 24px; height: 24px; background: var(--label-ink); }
</style>
</head>
<body>
  <main class="package">
    <div class="flower-pattern" role="img" aria-label="黒地に細い線で描かれた花模様"></div>
    <svg class="gold-scatter" viewBox="0 0 1200 2516" aria-hidden="true">
      <rect x="960" y="240" width="18" height="18" transform="rotate(20 969 249)"/>
      <rect class="light" x="972" y="292" width="12" height="12" transform="rotate(35 978 298)"/>
      <rect x="978" y="318" width="10" height="10"/>
      <rect x="860" y="472" width="14" height="14" transform="rotate(15 867 479)"/>
      <rect class="light" x="872" y="516" width="12" height="12" transform="rotate(40 878 522)"/>
      <rect x="834" y="600" width="10" height="10"/>
      <rect x="716" y="592" width="26" height="26" transform="rotate(25 729 605)"/>
      <rect x="700" y="712" width="16" height="16" transform="rotate(10 708 720)"/>
      <rect x="254" y="788" width="20" height="20" transform="rotate(30 264 798)"/>
      <rect class="light" x="214" y="830" width="14" height="14" transform="rotate(15 221 837)"/>
      <rect x="228" y="880" width="22" height="22" transform="rotate(40 239 891)"/>
      <rect x="150" y="866" width="12" height="12"/>
      <rect class="light" x="96" y="930" width="10" height="10" transform="rotate(25 101 935)"/>
      <rect x="64" y="980" width="14" height="14" transform="rotate(45 71 987)"/>
      <rect x="124" y="1010" width="10" height="10"/>
      <rect class="light" x="40" y="1060" width="12" height="12" transform="rotate(20 46 1066)"/>
    </svg>
    <div class="tea-band"></div>
    <div class="camellia camellia--top" role="img" aria-label="白い椿の花の挿絵"></div>
    <svg class="dewdrop" viewBox="0 0 40 60" aria-hidden="true">
      <path d="M20 0 C24 18 38 30 38 42 A18 18 0 0 1 2 42 C2 30 16 18 20 0 Z" fill="var(--drop)"/>
    </svg>
    <h1 class="product-name">しずくの里のおくりもの</h1>
    <div class="camellia camellia--bottom" role="img" aria-label="白い椿の花が三輪並ぶ挿絵"></div>
    <div class="maker-label"><span class="mark"></span><span class="maker-name">みどり園</span></div>
  </main>
</body>
</html>
```